Vro Klinieken website for a maxillofacial surgery clinic

It's a website for a clinic for maxillofacial surgery in WordPress . The website doesn't need to be complicated but has to look professional. It needs to be in Dutch so i can give the texts. Similar websites are www.tandartsenpraktijkvelmor.nl or www.tbospecialisten.nl. Pages would be sort of similar to https://hetcentrumvoorgezichtszorg.nl/ or https://wolderveenclinics.nl/. Those lasts are maxillofacial surgery clinic websites, but there are little more extensive.
I uploaded the logo. If this is not the proper quality i can upload the eps. Logo was made through printhive.

Target Market(s)

Patients who can find me and see information about the clinic

Industry/Entity Type

Healthcare

Coding

Coded - Design and coding required

Number of Pages Required

5+ page

Font styles to use
Other font styles liked:
• Something standard professional

Colors
0054AA
0677BA
7BADD7
CADEEF
E8F1F8

Requirements
Nice to have
• Something in line with the logo. I prefer a little dark like the darker logos but I'm not sure if that's professional. Logos zbpor and gvls are instances i'm registered to so they will have to be on the website too but small somewhere.

```html
<!DOCTYPE html>
<html lang="nl">
<head>
<meta charset="utf-8">
<title>Vro Klinieken – Kaakchirurgie</title>
<link href="https://fonts.googleapis.com/css2?family=Rubik:wght@500;600;700&family=Roboto:wght@300;400;500&display=swap" rel="stylesheet">
<style>
:root{
  --blue:#2ea3e0;
  --blue-dark:#0677ba;
  --slate:#6e84a3;
  --heading:#5b7193;
  --text:#8a929c;
  --ink:#222;
  --pale:#e8f1f8;
  --bg:#f7f8fa;
  --white:#fff;
}
*{box-sizing:border-box;margin:0;padding:0}
html,body{width:1200px;height:4935px;overflow:hidden}
body{font-family:"Roboto",sans-serif;color:var(--text);background:var(--bg);position:relative}
.abs{position:absolute}
h1,h2,h3{font-family:"Rubik",sans-serif;color:var(--heading)}
.photo{position:absolute}
p{font-size:13.5px;line-height:23px}

/* header */
.site-header{position:absolute;top:0;left:0;width:1200px;height:100px;background:var(--white)}
.brand{position:absolute;left:62px;top:28px;display:flex;align-items:center;gap:10px;font-family:"Rubik",sans-serif;font-weight:600;font-size:24px;color:var(--heading)}
.brand-dot{width:34px;height:34px;border-radius:50%;background:var(--blue)}
.nav{position:absolute;left:224px;top:50px;display:flex;gap:34px;font-size:13px;color:var(--heading)}
.nav .active{color:var(--blue)}
.phone-badge{position:absolute;left:720px;top:28px;width:48px;height:48px;border-radius:50%;background:var(--pale);display:flex;align-items:center;justify-content:center}
.phone-badge span{width:34px;height:34px;border-radius:50%;background:var(--blue);display:flex;align-items:center;justify-content:center}
.phone-num{position:absolute;left:790px;top:42px;font-size:15px;color:var(--heading)}
.btn{display:inline-flex;align-items:center;justify-content:center;background:var(--blue);color:#fff;border-radius:24px;font-size:13px;font-weight:500}
.header-cta{position:absolute;left:946px;top:31px;width:198px;height:42px;font-size:12px}

/* hero */
.hero{position:absolute;top:100px;left:0;width:1200px;height:550px;background:linear-gradient(90deg,#f4f6f8 0%,#e9edf1 45%,#b9c8d4 75%,#8ea3b4 100%)}
.hero h1{position:absolute;left:56px;top:102px;font-size:50px;line-height:60px;font-weight:700}
.hero p{position:absolute;left:56px;top:240px;width:420px;font-size:13.5px}
.hero .btn{position:absolute;left:56px;top:340px;width:116px;height:52px;font-size:14px}

/* features */
.feature{position:absolute;top:700px;width:360px;text-align:center}
.feature h3{font-family:"Roboto",sans-serif;font-weight:400;color:var(--ink);font-size:19px;margin:24px 0 14px}
.feature p{width:290px;margin:0 auto}
.feature .more{display:block;margin-top:22px;font-size:11px;color:#dde2e8}

/* about */
.eyebrow{font-size:15px;color:var(--blue)}
.about .eyebrow{position:absolute;left:56px;top:1098px}
.about h2{position:absolute;left:56px;top:1130px;width:410px;font-size:33px;line-height:37px}
.about p{position:absolute;left:56px;width:400px}

/* stats */
.stats{position:absolute;left:10px;top:1593px;width:1180px;height:220px;background:var(--slate);border-radius:4px}
.stat{position:absolute;top:48px;width:240px;text-align:center;color:#fff}
.stat .num{font-size:33px;font-weight:500;margin-top:16px}
.stat .lab{font-size:14px;margin-top:4px}

/* section titles */
.sec-title{position:absolute;left:0;width:1200px;text-align:center}
.sec-title .eyebrow{display:block}
.sec-title h2{font-size:32px;margin:10px 0 12px}
.sec-title p{width:490px;margin:0 auto}

/* services */
.service{position:absolute;top:2109px;width:346px;height:274px;background:#fff;box-shadow:0 4px 18px rgba(60,80,110,.10);padding:42px 46px}
.service.tint{background:var(--pale)}
.service h3{font-family:"Roboto",sans-serif;font-weight:400;color:var(--ink);font-size:19px;margin:12px 0 4px}
.service .link{font-size:12px;color:var(--blue);margin-top:8px;display:block}

/* team */
.member{position:absolute}
.member-overlay{position:absolute;left:18px;top:18px;right:18px;bottom:18px;background:rgba(40,45,55,.78);text-align:center;color:#fff}
.member-overlay .name{position:absolute;top:196px;width:100%;font-size:19px}
.member-overlay .role{position:absolute;top:238px;width:100%;font-size:14px;color:#c8ccd2}
.socials{position:absolute;top:272px;width:100%;display:flex;justify-content:center;gap:12px}
.socials span{width:24px;height:24px;border-radius:50%}

/* testimonial */
.testi{position:absolute;top:3144px;left:600px;width:600px;height:675px;background:var(--slate);text-align:center;color:#fff}
.testi .eyebrow{position:absolute;top:62px;width:100%;font-size:14px}
.testi h2{position:absolute;top:98px;width:100%;color:#fff;font-size:30px;font-weight:500}
.quote-mark{position:absolute;left:270px;top:172px;width:60px;height:60px;border-radius:50%;background:#fff;display:flex;align-items:center;justify-content:center}
.testi blockquote{position:absolute;left:100px;top:296px;width:400px;font-size:21px;line-height:34px;font-style:italic;font-weight:300}
.avatar{position:absolute;left:273px;top:462px;width:54px;height:54px;border-radius:50%;background:linear-gradient(#e8eaed,#9aa3ad);border:2px solid #fff}
.testi .who{position:absolute;top:538px;width:100%;font-size:14px;color:var(--blue)}
.testi .who-role{position:absolute;top:576px;width:100%;font-size:10px;color:#8d9db4}

/* faq */
.faq .eyebrow{position:absolute;left:56px;top:3904px}
.faq h2{position:absolute;left:56px;top:3940px;font-size:31px;font-weight:500}
.faq>p{position:absolute;left:56px;top:3998px;width:490px}
.q{position:absolute;left:56px;width:506px;height:56px;background:#fff;box-shadow:0 3px 14px rgba(60,80,110,.08);display:flex;align-items:center;justify-content:space-between;padding:0 28px 0 20px;font-size:14px;color:var(--ink)}
.q.open{background:var(--blue);color:#fff}
.answer{position:absolute;left:56px;top:4309px;width:506px;height:129px;background:#fff;box-shadow:0 3px 14px rgba(60,80,110,.08);padding:26px 36px}
.chat-circle{position:absolute;left:683px;top:4371px;width:114px;height:114px;border-radius:50%;background:#fff;box-shadow:0 4px 20px rgba(60,80,110,.15);display:flex;align-items:center;justify-content:center}

/* footer */
.site-footer{position:absolute;top:4562px;left:0;width:1200px;height:373px;background:var(--slate);color:#fff}
.foot-logo{position:absolute;left:56px;top:58px;width:162px;height:108px;background:#fff;display:flex;align-items:center;justify-content:center;gap:8px;font-family:"Rubik",sans-serif;font-weight:600;font-size:19px;color:var(--heading)}
.foot-logo span{width:22px;height:22px;border-radius:50%;background:var(--blue)}
.foot-about{position:absolute;left:56px;top:192px;width:290px;font-size:13px;line-height:22px}
.foot-col{position:absolute;top:60px}
.foot-col h4{font-weight:400;font-size:14px;color:var(--blue);margin-bottom:14px}
.foot-col li{list-style:none;font-size:13.5px;line-height:17px;margin-bottom:20px;padding-left:22px;position:relative}
.foot-col li::before{content:"";position:absolute;left:2px;top:5px;border-left:5px solid var(--blue);border-top:4px solid transparent;border-bottom:4px solid transparent}
.contact{position:absolute;left:836px;font-size:13.5px;display:flex;gap:14px;align-items:center}
.foot-btn{position:absolute;left:836px;top:191px;width:208px;height:46px;font-size:14px}
.foot-rule{position:absolute;left:56px;top:322px;width:1088px;height:1px;background:rgba(255,255,255,.25)}
.foot-social{position:absolute;left:60px;top:352px;display:flex;gap:14px}
.foot-social span{width:11px;height:11px;border-radius:50%;background:#fff}
.copy{position:absolute;left:928px;top:354px;font-size:11.5px}
</style>
</head>
<body>

<header class="site-header">
  <div class="brand"><span class="brand-dot"></span>Vro Klinieken</div>
  <nav class="nav">
    <span class="active">Home</span><span>Behandelingen</span><span>Vergoeding</span><span>Ons team</span><span>Folders</span>
  </nav>
  <div class="phone-badge"><span>
    <svg width="16" height="16" viewBox="0 0 24 24" fill="#fff"><path d="M6.6 10.8a15 15 0 006.6 6.6l2.2-2.2a1 1 0 011-.25 11.4 11.4 0 003.6.6 1 1 0 011 1V20a1 1 0 01-1 1A17 17 0 013 4a1 1 0 011-1h3.5a1 1 0 011 1c0 1.25.2 2.45.6 3.6a1 1 0 01-.25 1z"/></svg>
  </span></div>
  <div class="phone-num">(+31)20 555 0184</div>
  <span class="btn header-cta">MAAK EEN AFSPRAAK</span>
</header>

<section class="hero" role="img" aria-label="Foto van een tandarts met mondkapje die een behandellamp instelt">
  <h1>Welkom BIJ<br>Vro klinieken</h1>
  <p>Lorem ipsum dolor sit amet, consectetur adipiscing elit, sed do eiusmod tempor incididunt ut labore et dolore magna aliqua. Ut enim ad minim veniam</p>
  <span class="btn">Begin</span>
</section>

<section class="features">
  <div class="feature" style="left:52px">
    <svg width="46" height="46" viewBox="0 0 46 46" fill="none" stroke="var(--blue)" stroke-width="1.6"><circle cx="23" cy="22" r="14"/><path d="M17 23l4 4 8-9"/><path d="M16 35l-3 8 10-4 10 4-3-8"/></svg>
    <h3>Tevredenheidsgarantie</h3>
    <p>Lorem ipsum dolor sit amet, consect adipiscing elit, sed do eiusmod tempor incididunt ut labore et dolore magna aliqua</p>
    <span class="more">Lees meer →</span>
  </div>
  <div class="feature" style="left:420px">
    <svg width="46" height="46" viewBox="0 0 46 46" fill="none" stroke="var(--blue)" stroke-width="1.6"><path d="M8 40l6-6M12 38l20-20 4 4-20 20z"/><path d="M32 18l6-10M36 22l4-2"/></svg>
    <h3>Geweldige technologie</h3>
    <p>Lorem ipsum dolor sit amet, consect adipiscing elit, sed do eiusmod tempor incididunt ut labore et dolore magna aliqua</p>
    <span class="more">Lees meer →</span>
  </div>
  <div class="feature" style="left:790px">
    <svg width="46" height="46" viewBox="0 0 46 46" fill="none" stroke="var(--blue)" stroke-width="1.6"><circle cx="23" cy="14" r="7"/><path d="M10 42v-8a13 13 0 0126 0v8z"/><path d="M18 28v8M28 28v6"/></svg>
    <h3>Professionele tandarts</h3>
    <p>Lorem ipsum dolor sit amet, consect adipiscing elit, sed do eiusmod tempor incididunt ut labore et dolore magna aliqua</p>
    <span class="more">Lees meer →</span>
  </div>
</section>

<section class="about">
  <span class="eyebrow">OVER ONS</span>
  <h2>Beste tandheelkundige kliniek die u kunt vertrouwen</h2>
  <p style="top:1260px">Lorem ipsum dolor sit amet, consectetur adipiscing elit, sed do eiusmod tempor incididunt ut labore et dolore magna aliqua Ut enim ad minim veniam</p>
  <p style="top:1347px">Lorem ipsum dolor sit amet, consectetur adipiscing elit, sed do eiusmod tempor incididunt ut labore et dolore magna aliqua Ut enim ad minim veniam</p>
  <div class="photo" style="left:550px;top:1024px;width:311px;height:466px;background:linear-gradient(160deg,#e6e4e2,#b7c4c9 60%,#8fc9c7)" role="img" aria-label="Foto van een tandarts die een patiënte in de behandelstoel onderzoekt"></div>
  <div class="photo" style="left:893px;top:1035px;width:248px;height:368px;background:linear-gradient(160deg,#e3e6ea,#c9d6df 55%,#9fc6dc)" role="img" aria-label="Foto van een tandarts en een lachende patiënte tijdens een controle"></div>
  <span class="btn" style="position:absolute;left:928px;top:1434px;width:180px;height:44px;font-size:12px">Leer meer over ons</span>
</section>

<section class="stats">
  <div class="stat" style="left:54px">
    <svg width="46" height="46" viewBox="0 0 46 46" fill="none" stroke="var(--blue)" stroke-width="1.6"><circle cx="23" cy="23" r="19"/><circle cx="17" cy="19" r="1.5"/><circle cx="29" cy="19" r="1.5"/><path d="M15 27a9 9 0 0016 0"/></svg>
    <div class="num">1,452</div><div class="lab">Happy Patients</div>
  </div>
  <div class="stat" style="left:332px">
    <svg width="46" height="46" viewBox="0 0 46 46" fill="none" stroke="var(--blue)" stroke-width="1.6"><rect x="10" y="6" width="26" height="34" rx="2"/><path d="M16 16h14M16 22h14M16 28h8"/></svg>
    <div class="num">342</div><div class="lab">Online Appointments</div>
  </div>
  <div class="stat" style="left:608px">
    <svg width="46" height="46" viewBox="0 0 46 46" fill="none" stroke="var(--blue)" stroke-width="1.6"><circle cx="23" cy="20" r="13"/><path d="M23 12l2.5 5 5.5.8-4 3.9 1 5.5-5-2.6-5 2.6 1-5.5-4-3.9 5.5-.8z"/><path d="M15 31l-3 10 11-4 11 4-3-10"/></svg>
    <div class="num">15</div><div class="lab">Years Of Experience</div>
  </div>
  <div class="stat" style="left:884px">
    <svg width="46" height="46" viewBox="0 0 46 46" fill="none" stroke="var(--blue)" stroke-width="1.6"><circle cx="23" cy="12" r="7"/><path d="M10 42v-10a13 13 0 0126 0v10z"/><path d="M23 26v14"/></svg>
    <div class="num">72</div><div class="lab">Doctors and Staff</div>
  </div>
</section>

<section class="services">
  <div class="sec-title" style="top:1914px">
    <span class="eyebrow">Behandelingen</span>
    <h2>Welke service wij bieden</h2>
    <p>Lorem ipsum dolor sit amet, consectetur adipiscing elit, sed do eiusmod tempor incididunt ut labore et dolore magna aliqua</p>
  </div>
  <div class="service tint" style="left:56px">
    <svg width="36" height="36" viewBox="0 0 36 36" fill="none" stroke="var(--blue)" stroke-width="1.5"><path d="M10 4c-5 0-7 5-5 11l3 16c1 2 3 2 4 0l2-8h4l2 8c1 2 3 2 4 0l3-16c2-6 0-11-5-11-3 0-4 2-7 2s-4-2-5-2z"/></svg>
    <h3>KAAKCHIRURGIE</h3>
    <p>Lorem ipsum dolor sit amet, consec adipiscing elit, sed do eiusmod tempor incididunt ut labore et dolore magna aliqua</p>
    <span class="link">LEES MEER →</span>
  </div>
  <div class="service" style="left:427px">
    <svg width="36" height="36" viewBox="0 0 36 36" fill="none" stroke="var(--blue)" stroke-width="1.5"><path d="M10 4c-5 0-7 5-5 11l3 16c1 2 3 2 4 0l2-8h4l2 8c1 2 3 2 4 0l3-16c2-6 0-11-5-11-3 0-4 2-7 2s-4-2-5-2z"/></svg>
    <h3>VERWIJSPRAKTIJK</h3>
    <p>Lorem ipsum dolor sit amet, consec adipiscing elit, sed do eiusmod tempor incididunt ut labore et dolore magna aliqua</p>
    <span class="link">LEES MEER →</span>
  </div>
  <div class="service" style="left:799px">
    <svg width="36" height="36" viewBox="0 0 36 36" fill="none" stroke="var(--blue)" stroke-width="1.5"><rect x="4" y="6" width="22" height="26"/><path d="M9 13h12M9 19h12M9 25h7"/><path d="M26 4h6v10h-6"/></svg>
    <h3>VERWIJZER</h3>
    <p>Lorem ipsum dolor sit amet, consec adipiscing elit, sed do eiusmod tempor incididunt ut labore et dolore magna aliqua</p>
    <span class="link">LEES MEER →</span>
  </div>
</section>

<section class="team">
  <div class="sec-title" style="top:2502px">
    <span class="eyebrow">Ons Team</span>
    <h2>Team van professionals</h2>
    <p style="width:560px">Lorem ipsum dolor sit amet, consectetur adipiscing elit, sed do eiusmod tempor incididunt ut labore et dolore magna aliqua</p>
  </div>
  <div class="member" style="left:48px;top:2688px;width:360px;height:354px;background:linear-gradient(160deg,#dfe3e7,#b9c2ca)" role="img" aria-label="Portretfoto van orthodontist in witte jas">
    <div class="member-overlay">
      <div class="name">Lotte Verhaar</div>
      <div class="role">Orthodontist</div>
      <div class="socials"><span style="background:var(--blue)"></span><span style="background:#2ec1d8"></span><span style="background:#21b28a"></span></div>
    </div>
  </div>
  <div class="member" style="left:427px;top:2697px;width:346px;height:338px;background:linear-gradient(160deg,#eef0f2,#cdd6dc)" role="img" aria-label="Portretfoto van tandarts met veiligheidsbril in een behandelkamer"></div>
  <div class="member" style="left:799px;top:2697px;width:345px;height:338px;background:linear-gradient(160deg,#eef1f3,#cfd8de)" role="img" aria-label="Portretfoto van kaakchirurg in witte jas in een behandelkamer"></div>
</section>

<div class="photo" style="left:0;top:3144px;width:600px;height:675px;background:linear-gradient(160deg,#e9eef2,#b8cfe0 50%,#d9a86a 85%)" role="img" aria-label="Foto van een tandarts en een tevreden patiënt die een duim opsteekt"></div>
<section class="testi">
  <span class="eyebrow">Testimonial</span>
  <h2>Wat de klant zegt</h2>
  <div class="quote-mark"><svg width="24" height="20" viewBox="0 0 24 20" fill="var(--slate)"><path d="M0 20V11C0 5 3 1 9 0v4c-3 1-4 3-4 6h4v10zM14 20V11c0-6 3-10 9-11v4c-3 1-4 3-4 6h4v10z"/></svg></div>
  <blockquote>"Lorem ipsum dolor sit amet, consectetur adipiscing elit, sed do eiusmod tempor incididunt ut labore et dolore magna aliqua minim veniam"</blockquote>
  <div class="avatar" role="img" aria-label="Profielfoto van de klant"></div>
  <div class="who">Daan Willemse</div>
  <div class="who-role">Patiënt</div>
</section>

<section class="faq">
  <span class="eyebrow">FAQ</span>
  <h2>VEEL GESTELDE VRAGEN</h2>
  <p>Lorem ipsum dolor sit amet, consectetur adipiscing elit, sed do eiusmod tempor incididunt ut labore et dolore magna aliqua</p>
  <div class="q" style="top:4094px">Waarvoor kan ik terecht bij de kaakchirurg?<svg width="14" height="9" viewBox="0 0 14 9" fill="none" stroke="var(--blue)" stroke-width="2"><path d="M1 1l6 6 6-6"/></svg></div>
  <div class="q" style="top:4173px">Wat is het verschil tussen de tandarts en de kaakchirurg?<svg width="14" height="9" viewBox="0 0 14 9" fill="none" stroke="var(--blue)" stroke-width="2"><path d="M1 1l6 6 6-6"/></svg></div>
  <div class="q open" style="top:4254px">Ik ben doorverwezen naar de kaakchirurg, wat nu?<svg width="14" height="9" viewBox="0 0 14 9" fill="none" stroke="#fff" stroke-width="2"><path d="M1 8l6-6 6 6"/></svg></div>
  <div class="answer"><p>Lorem ipsum dolor sit amet, consectetuer adipiscing elit. Aenean commodo ligula eget dolor. Aenean massa. Cum sociis natoque penatibus et magnis dis parturient montes</p></div>
  <div class="abs" style="left:709px;top:3995px;width:426px;height:474px;background:#d5dde6"></div>
  <div class="photo" style="left:677px;top:3937px;width:398px;height:468px;background:linear-gradient(160deg,#f2f4f6,#cfdae3 55%,#7e9bb8)" role="img" aria-label="Foto van een kaakchirurg met tandheelkundig instrument naast een patiënt"></div>
  <div class="chat-circle"><svg width="42" height="34" viewBox="0 0 42 34" fill="none" stroke="var(--blue)" stroke-width="1.6"><path d="M2 2h24v16H12l-6 5v-5H2z"/><path d="M30 10h10v16h-4v5l-6-5H16v-4"/></svg></div>
</section>

<footer class="site-footer">
  <div class="foot-logo"><span></span>Vro Klinieken</div>
  <p class="foot-about">Lorem ipsum dolor sit amet, consectetur adipiscing elit, sed do eiusmod tempor incididunt ut labore et dolore</p>
  <div class="foot-col" style="left:404px">
    <h4>Snelle koppelingen</h4>
    <ul><li>Home</li><li>Behandelingen</li><li>Vergoeding</li><li>Ons team</li><li>Folders</li></ul>
  </div>
  <div class="foot-col" style="left:634px">
    <h4>Behandelingen</h4>
    <ul><li>KAAKCHIRURGIE</li><li>VERWIJSPRAKTIJK</li><li>VERWIJZER</li><li>CHIRURGISCHE<br>ENDODONTIE</li></ul>
  </div>
  <div class="foot-col" style="left:836px"><h4>Een afspraak maken</h4></div>
  <div class="contact" style="top:101px"><svg width="12" height="14" viewBox="0 0 12 14" fill="var(--blue)"><path d="M6 0a6 6 0 016 6c0 4-6 8-6 8S0 10 0 6a6 6 0 016-6zm0 4a2 2 0 100 4 2 2 0 000-4z"/></svg>Lindenlaan 14, Amersfoort</div>
  <div class="contact" style="top:137px"><svg width="13" height="10" viewBox="0 0 13 10" fill="var(--blue)"><path d="M0 0h13v10H0z"/></svg>info@vroklinieken.nl</div>
  <span class="btn foot-btn">
    <svg width="13" height="13" viewBox="0 0 24 24" fill="#fff" style="margin-right:6px"><path d="M6.6 10.8a15 15 0 006.6 6.6l2.2-2.2a1 1 0 011-.25 11.4 11.4 0 003.6.6 1 1 0 011 1V20a1 1 0 01-1 1A17 17 0 013 4a1 1 0 011-1h3.5a1 1 0 011 1c0 1.25.2 2.45.6 3.6a1 1 0 01-.25 1z"/></svg>(+31)20 555 0185</span>
  <div class="foot-rule"></div>
  <div class="foot-social"><span></span><span></span><span></span></div>
  <div class="copy">Copyright © 2023. All Right Reserved.</div>
</footer>

</body>
</html>
```